Home Page Design

We have a B2B home page design and need a consumer version. The look and feel can look similar but needs to be distinctly different so it in not to get confused. Essentially it should look like the same company with a different model. We will need a PSD w all layers organized and easy to understand. Attached is the logo, B2B comp, and a MS Word doc with a short description. In addition, I have attached a wire frame to be used as a site map. PLEASE DO NOT take that as the creative. I expect to see your creative based on the information provided.

Consumer

```html
<!DOCTYPE html>
<html lang="en">
<head>
<meta charset="utf-8">
<title>GivingHost.com – Home</title>
<link href="https://fonts.googleapis.com/css2?family=Raleway:wght@400;500&family=Arimo:wght@400;700&family=Lato:ital,wght@1,400;1,700&display=swap" rel="stylesheet">
<style>
:root{
  --brand-blue:#1a6a93;
  --blue-light:#1c8cc4;
  --blue-dark:#125f86;
  --brand-green:#3cb544;
  --green-dark:#2f9a37;
  --ink:#222;
  --muted:#3a3a3a;
  --panel:#efefef;
  --frame:#c9c9c9;
  --quote-red:#d0202a;
  --white:#fff;
}
*{box-sizing:border-box;margin:0;padding:0}
html,body{width:1034px;height:1200px;overflow:hidden;background:var(--white)}
body{font-family:"Arimo",Arial,sans-serif;color:var(--ink)}
.page{position:relative;width:948px;height:1100px;transform:scale(1.0907);transform-origin:0 0}
.abs{position:absolute}

.top-rule{left:0;top:0;width:948px;height:5px;background:var(--brand-blue)}

.brand{left:80px;top:22px;display:flex;align-items:center;gap:10px}
.brand-mark{width:56px;height:56px;border-radius:50%;background:var(--brand-blue)}
.brand-name{font-family:"Raleway",sans-serif;font-weight:500;font-size:22px;color:var(--brand-green)}

.main-nav{left:407px;top:43px;display:flex;align-items:center;font-size:12.5px;text-transform:uppercase}
.main-nav a{color:var(--ink);text-decoration:none;margin-right:27px;line-height:23px}
.main-nav a.active{background:var(--brand-green);color:var(--white);padding:0 11px;border-radius:3px;margin-right:14px}

.hero-side{top:105px;height:357px;background:linear-gradient(180deg,#d4d4d4,#a9a9a9)}
.hero-side.left{left:0;width:118px}
.hero-side.right{left:834px;width:114px;background:linear-gradient(180deg,#e8e8e8,#bdbdbd)}
.hero-photo{left:118px;top:105px;width:716px;height:357px;background:linear-gradient(135deg,#4a3a34 0%,#2d3f73 45%,#6c6f86 70%,#3a2f2c 100%)}
.hero-arrow{top:272px;width:28px;height:28px;background:#3b3b3b;display:flex;align-items:center;justify-content:center}
.hero-dots{left:456px;top:444px;display:flex;gap:6px}
.hero-dots span{width:6px;height:6px;border-radius:50%;background:#8a8a8a}
.hero-dots span.on{background:#e0b12b}

.auction-form{left:79px;top:495px;width:184px;height:245px;border-radius:18px;background:linear-gradient(90deg,var(--blue-dark),var(--blue-light));box-shadow:0 6px 6px -3px rgba(0,0,0,.25);padding:18px 11px}
.auction-form h2{font-family:"Raleway",sans-serif;font-weight:500;font-size:19px;color:var(--white);margin-bottom:14px}
.field{display:block;width:151px;height:24px;background:var(--white);font-size:12px;color:#999;padding:5px 6px;margin-bottom:16px}
.btn-submit{margin:4px 0 0 62px;width:90px;height:29px;background:var(--brand-green);color:var(--white);border-radius:4px;font-family:"Raleway",sans-serif;font-size:18px;display:flex;align-items:center;justify-content:center}

.welcome{left:294px;top:507px;width:544px}
.welcome h1{font-family:"Raleway",sans-serif;font-weight:400;font-size:22px;color:var(--brand-green);margin-bottom:14px}
.welcome p{font-size:11.3px;line-height:17.5px;color:var(--muted);padding-left:3px;margin-bottom:17px}
.btn-more{left:758px;top:706px;width:77px;height:25px;background:var(--brand-green);color:var(--white);border-radius:4px;font-size:11.5px;display:flex;align-items:center;justify-content:center}

.section-title{font-family:"Raleway",sans-serif;font-weight:500;font-size:19px;color:var(--ink);top:780px}
.items-strip{left:91px;top:822px;width:509px;height:156px;background:var(--panel)}
.item-thumb{top:835px;height:131px;border:3px solid var(--frame)}
.strip-tab{top:878px;width:41px;height:34px;background:linear-gradient(#fff,#ddd);box-shadow:0 2px 3px rgba(0,0,0,.3);display:flex;align-items:center;justify-content:center}
.strip-tab.left{left:81px;border-radius:0 17px 17px 0}
.strip-tab.right{left:568px;border-radius:17px 0 0 17px}

.golf-box{left:647px;top:823px;width:207px;height:157px;background:#f6f6f6;border:1px solid #ddd}
.golf-bar{left:647px;width:207px;height:22px;background:var(--frame);display:flex;align-items:center;justify-content:center}
.quote{left:655px;display:flex;gap:6px;width:190px}
.avatar{flex:none;background:linear-gradient(135deg,#8a6a4a,#c9a47a)}
.quote p{font-family:"Lato",sans-serif;font-style:italic;font-size:9.5px;line-height:12px;color:var(--ink)}
.quote b{color:var(--quote-red);font-weight:700}
.quote-rule{left:655px;top:905px;width:186px;height:1px;background:#d4d4d4}

.site-footer{left:0;top:1021px;width:948px;height:79px;background:var(--brand-green);color:var(--white)}
.footer-links{left:89px;top:1046px;display:flex;font-family:"Raleway",sans-serif;font-size:12px}
.footer-links span{margin-right:23px}
.copyright{left:90px;top:1072px;font-size:11px}
.footer-brand{left:671px;top:1038px;display:flex;align-items:center;gap:10px}
.footer-brand .brand-mark{width:52px;height:52px;background:var(--white);opacity:.9}
.footer-brand .brand-name{color:var(--white);font-size:19px}
</style>
</head>
<body>
<div class="page">
  <div class="abs top-rule"></div>

  <header>
    <div class="abs brand"><span class="brand-mark"></span><span class="brand-name">GivingHost.com</span></div>
    <nav class="abs main-nav">
      <a class="active" href="#">Home</a><a href="#">Post Your Event</a><a href="#">Add Auction Items</a><a href="#">About</a><a href="#">Contact</a>
    </nav>
  </header>

  <section class="hero">
    <div class="abs hero-side left" role="img" aria-label="Faded photo of a smiling child"></div>
    <div class="abs hero-photo" role="img" aria-label="Photo of schoolchildren in uniforms praying together"></div>
    <div class="abs hero-side right" role="img" aria-label="Faded photo of the next slide"></div>
    <div class="abs hero-arrow" style="left:70px"><svg width="10" height="14"><path d="M8 1 2 7l6 6" fill="none" stroke="#fff" stroke-width="2"/></svg></div>
    <div class="abs hero-arrow" style="left:853px"><svg width="10" height="14"><path d="M2 1l6 6-6 6" fill="none" stroke="#fff" stroke-width="2"/></svg></div>
    <div class="abs hero-dots"><span></span><span></span><span class="on"></span></div>
  </section>

  <form class="abs auction-form">
    <h2>An Auction Item:</h2>
    <span class="field">Auction Type</span>
    <span class="field">Auction Date</span>
    <span class="field">Auction Date</span>
    <div class="btn-submit">Submit</div>
  </form>

  <section class="abs welcome">
    <h1>Welcome to Giving Host</h1>
    <p>Lorem Ipsum is simply dummy text of the printing and. Typesetting industry. Lorem Ipsum has been the industry's standard dummy text ever since the 1500s, when an unknown printer took a galley of type and scrambled it to make a type specimen book.</p>
    <p>but also the leap into electronic typesetting, remaining essentially unchanged. It was popularised in the 1960s with the releasesimply dummy text of the printing and typesetting industry. Lorem Ipsum has been the industry's standard dummy text ever since the 1500s, when an unknown printer took a galley of type and scrambled it to make a type specimen book. It has survived not only five centuries</p>
  </section>
  <div class="abs btn-more">read more</div>

  <h2 class="abs section-title" style="left:89px">Auction Items</h2>
  <div class="abs items-strip"></div>
  <div class="abs item-thumb" style="left:135px;width:97px;background:linear-gradient(135deg,#5a4a44,#9a2a2a)" role="img" aria-label="Photo of guests at a charity dinner"></div>
  <div class="abs item-thumb" style="left:243px;width:96px;background:linear-gradient(90deg,#fafafa,#3a3a2a 40%,#6a6a3a 80%,#fafafa)" role="img" aria-label="Photo of wine bottles"></div>
  <div class="abs item-thumb" style="left:350px;width:96px;background:linear-gradient(135deg,#fff,#9fb6cc 50%,#fff)" role="img" aria-label="Photo of a road bicycle"></div>
  <div class="abs item-thumb" style="left:458px;width:96px;background:linear-gradient(180deg,#9ab0c4,#c8b79a 50%,#6a5e52)" role="img" aria-label="Photo of a city street"></div>
  <div class="abs strip-tab left"><svg width="10" height="12"><path d="M2 1l6 5-6 5z" fill="#333"/></svg></div>
  <div class="abs strip-tab right"><svg width="10" height="12"><path d="M8 1 2 6l6 5z" fill="#333"/></svg></div>

  <h2 class="abs section-title" style="left:644px">Featured Golf Event</h2>
  <div class="abs golf-box"></div>
  <div class="abs golf-bar" style="top:823px"><svg width="16" height="10"><path d="M2 9l6-6 6 6" fill="none" stroke="#111" stroke-width="3"/></svg></div>
  <div class="abs quote" style="top:855px"><span class="avatar" style="width:38px;height:38px" role="img" aria-label="Portrait of a customer"></span><p>"Lost Over 80 Pounds in 8 Months Without Working Out!"<br><b>- Marta L.</b></p></div>
  <div class="abs quote-rule"></div>
  <div class="abs quote" style="top:915px;left:658px"><span class="avatar" style="width:32px;height:32px" role="img" aria-label="Portrait of a customer"></span><p>"Lost Over 50 Pounds &amp; My Cholesterol Dropped 50 Points!"<br><b>-Dana R.</b></p></div>
  <div class="abs golf-bar" style="top:958px"><svg width="16" height="10"><path d="M2 1l6 6 6-6" fill="none" stroke="#111" stroke-width="3"/></svg></div>

  <footer class="abs site-footer"></footer>
  <div class="abs footer-links" style="color:var(--white)"><span>Post Your event</span><span>|</span><span>Add Auction items</span><span>|</span><span>About</span><span>|</span><span>Contact</span></div>
  <div class="abs copyright" style="color:var(--white)">Copyright © 2014 All Rights Reserved | Privacy Policy</div>
  <div class="abs footer-brand"><span class="brand-mark"></span><span class="brand-name">GivingHost.com</span></div>
</div>
</body>
</html>
```